Artistic Poster for a Short Film

I am the Writer/Director of an upcoming short film called "Driftwater" and I need a 20x30 poster for the project screening. The screening is coming up very soon so apologies for the quick turnaround time. Here is a short synopsis:

"Walter is a mysterious man who is lost and disoriented. With the help of Marisol, he searches for items out of an old diary written long ago by a woman named Gloria, despite not understanding exactly why he does so. Marisol helps, but when they are unsuccessful she confronts Walter: Does he know why he restlessly searches for these items? The truth is shocking, and reveals Walter's connections to Marisol, Gloria, and the strange old diary.

The truth is that Walter is actually an old man, and Marisol is his caretaker and granddaughter. His memories, including those of Gloria, his deceased wife, have been destroyed by Dementia. He often wakes believing himself to be at an earlier stage of his life, and therefore meets many of the challenges of life with anger and confusion."

Here is the film's website: http://www.driftwater-film.example
Here is our successful Fundbarrow: http://www.fundbarrow.example/projects/502847719/driftwater-a-short-film

The design should be dark and simple. I'm a fan of the art-prints that this short film used (scroll down to see): http://www.fundbarrow.example/projects/ruthvanderlo/kettle-a-short-film-based-on-the-story-by-omar-quill but I'm also open to other ideas. If you google "alternative movie posters" you'll see what I mean. The poster should be simple, easy to read, and hint at the themes of the film without giving the twist away.

Here is a link to the Fine Cut of the film: https://clipvault.example/48210576 The password is: lanterns72
It is not a completed version but will give you an idea of what the film will look like.

Target Market(s)

The intended audience is an art-film crowd of moviegoers.

Industry/Entity Type

Movie

Requirements
Must have
• The poster must have the typical movie poster text at the bottom. The information that should be included is: First line: COPPER LANTERN STUDIOS presents a film by DANIEL OSTROM "DRIFTWATER" MARCEL BRUNAUD TERRA WOLCOTT
Second line: music by OWEN PRATT director of photography VICTOR L. MORALES edited by SIMON ORR costume designer ROBERTA CLINE
Third line: produced by GAIL TORVALD DANIEL OSTROM written and directed by DANIEL OSTROM

It should have the title of the film "Driftwater" and "A film by Daniel Ostrom" on the poster (in addition to the text at the bottom.

It must be high-quality and printable to a size of 20x30. Ideal resolution is 6060x9090. I only need the high quality printable file, I will do the printing myself.
Should not have
• Bright colors.

```html
<!DOCTYPE html>
<html lang="en">
<head>
<meta charset="utf-8">
<title>Driftwater — Poster</title>
<link rel="stylesheet" href="https://fonts.googleapis.com/css2?family=Cormorant+Garamond:wght@500;600&family=Gentium+Book+Plus&family=Tinos&display=swap">
<style>
  :root {
    --ink: #ffffff;
    --night: #060102;
    --ember: #1c0507;
    --glow: #4a0e13;
    --haze: #2a1416;
  }
  * { margin: 0; padding: 0; box-sizing: border-box; }
  html, body { width: 800px; height: 1200px; overflow: hidden; background: var(--night); }
  .poster {
    position: relative;
    width: 800px;
    height: 1200px;
    overflow: hidden;
    color: var(--ink);
    text-align: center;
  }
  .backdrop {
    position: absolute;
    inset: 0;
    background:
      radial-gradient(ellipse 70px 75px at 22px 860px, rgba(255,245,245,0.95), rgba(240,190,190,0.5) 55%, transparent 100%),
      radial-gradient(ellipse 130px 120px at 40px 800px, rgba(150,30,36,0.45), transparent 75%),
      radial-gradient(ellipse 110px 150px at 690px 420px, rgba(95,18,24,0.55), transparent 75%),
      radial-gradient(ellipse 380px 90px at 420px 640px, rgba(70,16,20,0.6), transparent 80%),
      radial-gradient(ellipse 260px 70px at 650px 600px, rgba(90,80,82,0.25), transparent 80%),
      radial-gradient(ellipse 200px 220px at 220px 330px, rgba(60,10,14,0.45), transparent 75%),
      radial-gradient(ellipse 160px 120px at 90px 140px, rgba(70,12,16,0.4), transparent 75%),
      linear-gradient(180deg, var(--night) 0%, var(--ember) 30%, var(--ember) 48%, var(--glow) 55%, var(--haze) 62%, var(--ember) 75%, var(--night) 90%);
  }
  .tagline {
    position: absolute;
    top: 78px;
    left: 0;
    right: 0;
    font-family: "Gentium Book Plus", serif;
    font-size: 35px;
    line-height: 44px;
  }
  .title {
    position: absolute;
    top: 476px;
    left: 0;
    right: 0;
    font-family: "Gentium Book Plus", serif;
    font-weight: 400;
    font-size: 98px;
    letter-spacing: 4px;
    line-height: 1;
  }
  .byline {
    position: absolute;
    top: 564px;
    left: 0;
    right: 0;
    font-family: "Cormorant Garamond", serif;
    font-weight: 600;
    font-size: 34px;
    padding-left: 24px;
  }
  .billing {
    position: absolute;
    top: 1008px;
    left: 0;
    right: 0;
    font-family: "Tinos", serif;
    color: var(--ink);
  }
  .billing-line {
    display: block;
    white-space: nowrap;
    transform: scaleX(0.6);
    transform-origin: center;
    line-height: 34px;
    margin: 0 -300px;
    color: var(--ink);
  }
  .billing .big { font-size: 25px; color: var(--ink); }
  .billing .small { font-size: 16px; color: var(--ink); }
</style>
</head>
<body>
  <main class="poster">
    <div class="backdrop" role="img" aria-label="Blurred night street with red bokeh lights and a bright car headlight glowing in the dark"></div>

    <p class="tagline">“Sometimes a dark cloud rolls overhead and<br>takes away things you cant ever get back”</p>

    <h1 class="title">DRIFTWATER</h1>
    <p class="byline">A film by Daniel Ostrom</p>

    <footer class="billing">
      <span class="billing-line"><span class="big">COPPER LANTERN STUDIOS</span> <span class="small">presents a film by</span> <span class="big">DANIEL OSTROM "DRIFTWATER" MARCEL BRUNAUD TERRA WOLCOTT</span></span>
      <span class="billing-line"><span class="small">music by</span> <span class="big">OWEN PRATT</span> <span class="small">director of photography</span> <span class="big">VICTOR L. MORALES</span> <span class="small">edited by</span> <span class="big">SIMON ORR</span> <span class="small">costume designer</span> <span class="big">ROBERTA CLINE</span></span>
      <span class="billing-line"><span class="small">produced by</span> <span class="big">GAIL TORVALD DANIEL OSTROM</span> <span class="small">written and directed by</span> <span class="big">DANIEL OSTROM</span></span>
    </footer>
  </main>
</body>
</html>
```